Premium modern eliquids labels 84.5 x 80 mm

I am looking for modern graphics for the labels of a new eliquid line that will have 4 different types of eliquids. It will have a tobacco one (brown colours maybe), a fruity one (bright colours maybe), a minty one (green colours maybe) and a creamy one (beige colours maybe).
I will need one of them to see how the design is, that design will have to be adapted to the other 3 colours of the label.
The brand logo is attached. I also attached a sample of what is mandatory to write on the label, you can change size, place and font of what is written, the only thing that cannot be reduced is the yellow parts. I attach the bottle that we will use.The size of the label is 84.5 x 80 mm (base x height).

Target Market(s)

vapers

Requirements
Must have
• My project must have one of the labels.

```html
<!DOCTYPE html>
<html lang="en">
<head>
<meta charset="utf-8">
<title>Kestrel Vape – Premium Eliquids Label Range</title>
<link rel="stylesheet" href="https://fonts.googleapis.com/css2?family=Tulpen+One&display=swap">
<style>
  :root {
    --backdrop: #c4c4c4;
    --label-black: #000000;
    --ink-white: #ffffff;
    --tobacco: #e0792a;
    --tobacco-deep: #c2631c;
    --fruity: #f28b82;
    --fruity-deep: #e06f66;
    --minty: #44bd6e;
    --minty-deep: #2f9e58;
    --creamy: #fbefc6;
    --creamy-deep: #e8d9a8;
  }
  * { margin: 0; padding: 0; box-sizing: border-box; }
  html, body {
    width: 1200px;
    height: 892px;
    overflow: hidden;
    background: var(--backdrop);
  }
  .label-range {
    position: relative;
    width: 1200px;
    height: 892px;
  }
  .label {
    position: absolute;
    top: 348px;
    width: 154px;
    height: 410px;
    background: var(--label-black);
    overflow: hidden;
    font-family: "Tulpen One", sans-serif;
    text-align: center;
  }
  .label--tobacco { left: 119px; --accent: var(--tobacco); --accent-deep: var(--tobacco-deep); }
  .label--fruity  { left: 379px; --accent: var(--fruity);  --accent-deep: var(--fruity-deep); }
  .label--minty   { left: 633px; --accent: var(--minty);   --accent-deep: var(--minty-deep); }
  .label--creamy  { left: 902px; --accent: var(--creamy);  --accent-deep: var(--creamy-deep); }

  .brand-name {
    position: absolute;
    top: 64px;
    left: 0;
    width: 100%;
    font-size: 30px;
    line-height: 1;
    letter-spacing: 1px;
    color: var(--accent);
  }
  .flavour-name {
    position: absolute;
    top: 132px;
    left: 0;
    width: 100%;
    font-size: 80px;
    line-height: 1;
    color: var(--accent);
  }
  .product-line {
    position: absolute;
    top: 206px;
    left: 0;
    width: 100%;
    font-size: 25px;
    line-height: 1;
    color: var(--ink-white);
  }
  .pattern-area {
    position: absolute;
    left: 0;
    bottom: 0;
    width: 100%;
    height: 162px;
    background: linear-gradient(to bottom, var(--label-black) 0%, var(--accent-deep) 160%);
    opacity: 0.85;
  }
</style>
</head>
<body>
  <main class="label-range">
    <section class="label label--tobacco">
      <p class="brand-name">KESTREL VAPE</p>
      <h2 class="flavour-name">TOBACCO</h2>
      <p class="product-line">Premium Eliquids</p>
      <div class="pattern-area" role="img" aria-label="Decorative pattern of overlapping outlined circles in tobacco orange"></div>
    </section>
    <section class="label label--fruity">
      <p class="brand-name">KESTREL VAPE</p>
      <h2 class="flavour-name">FRUITY</h2>
      <p class="product-line">Premium Eliquids</p>
      <div class="pattern-area" role="img" aria-label="Decorative pattern of overlapping outlined circles in fruity pink"></div>
    </section>
    <section class="label label--minty">
      <p class="brand-name">KESTREL VAPE</p>
      <h2 class="flavour-name">MINTY</h2>
      <p class="product-line">Premium Eliquids</p>
      <div class="pattern-area" role="img" aria-label="Decorative pattern of overlapping outlined circles in mint green"></div>
    </section>
    <section class="label label--creamy">
      <p class="brand-name">KESTREL VAPE</p>
      <h2 class="flavour-name">CREAMY</h2>
      <p class="product-line">Premium Eliquids</p>
      <div class="pattern-area" role="img" aria-label="Decorative pattern of overlapping outlined circles in cream beige"></div>
    </section>
  </main>
</body>
</html>
```